Chiropractic healthcare group business card

We are a Portland Oregon based chiropractic healthcare group. Looking for a new business card design. Something cutting edge, that shows off our new logo and tag line.Use either of the attached logos.Our tag line = "Who would you be without pain?"I'm open to about anything, impress me!!
Target Market(s)
Chiropractic patients - Auto injury, back pain, sports injuries, neck , shoulder, hip, knee, ankle pain.
Industry/Entity Type
Chiropractic
Contact Information for Business Card
Dr. Bram Holtvick, D.C.
Clinic name - Fernway Chiropractic
2 clinics
location #1
20418 NW Marwick Road
Suite B
North Plains, OR 97133
Location #2
13529 SE Calloway Street
Portland OR 97236
Main phone line 971.555.0143
website : www.FernwayClinics.example
Tag line "Who would you be without pain?"
Colors
Designer to choose colors to be used in the design.
Requirements
Must have
- Use the logo colors -- Want the orange color to be a TRUE orange.
- Both clinic address
- phone number
- website
- personal email - b.holtvick@ReliefBeginsHere.example
- tag line - "Who would you be without pain?"

```html
<!DOCTYPE html>
<html lang="en">
<head>
<meta charset="utf-8">
<title>Fernway Chiropractic – Business Card</title>
<link rel="stylesheet" href="https://fonts.googleapis.com/css2?family=Crimson+Text:wght@400;600;700&family=Alegreya:wght@500;700&display=swap">
<style>
  :root {
    --backdrop: #666666;
    --card-orange: #c55a47;
    --card-grey: #d7d4d7;
    --ink: #2b2a2b;
    --ink-soft: #3c3b3d;
    --accent: #c9502f;
    --rule-grey: #a9a6aa;
  }
  * { margin: 0; padding: 0; box-sizing: border-box; }
  html, body {
    width: 1200px; height: 1200px; overflow: hidden;
    background: var(--backdrop);
  }
  .canvas { position: relative; width: 1200px; height: 1200px; }
  .card { position: absolute; width: 672px; height: 384px; }
  .card > * { position: absolute; line-height: 1; white-space: nowrap; }

  /* front */
  .card--front { left: 50px; top: 139px; background: var(--card-orange); }
  .brand { font-family: "Crimson Text", serif; font-weight: 700; color: var(--ink); }
  .card--front .brand-name { left: 0; width: 672px; text-align: center; top: 78px; font-size: 54px; letter-spacing: 0.28em; }
  .card--front .brand-sub { left: 0; width: 672px; text-align: center; top: 146px; font-size: 18px; letter-spacing: 0.35em; }
  .front-rule { left: 48px; top: 264px; width: 578px; height: 2px; background: var(--ink); }
  .tagline {
    left: 0; width: 672px; text-align: center; top: 278px;
    font-family: "Crimson Text", serif; font-weight: 600; font-size: 19px;
    letter-spacing: 0.26em; color: var(--ink);
  }
  .website {
    left: 0; width: 672px; text-align: center; top: 311px;
    font-family: "Crimson Text", serif; font-weight: 700; font-size: 21px;
    letter-spacing: 0.14em; color: #1e1d1e;
  }

  /* back */
  .card--back { left: 458px; top: 685px; background: var(--card-grey); }
  .card--back .brand-name { left: 34px; top: 58px; font-size: 34px; letter-spacing: 0.24em; }
  .card--back .brand-sub { left: 36px; top: 96px; font-size: 11px; letter-spacing: 0.28em; }
  .clinic-block {
    right: 12px; top: 50px; text-align: center;
    font-family: "Crimson Text", serif; font-weight: 700; font-size: 13px;
    letter-spacing: 0.2em; line-height: 20px; color: var(--ink);
  }
  .clinic-block .doctor { color: var(--accent); }
  .divider-v { left: 350px; top: 150px; width: 2px; height: 196px; background: var(--rule-grey); }
  .rule { height: 2px; background: var(--rule-grey); }
  .rule--phone-top { left: 49px; top: 197px; width: 298px; }
  .rule--phone-bottom { left: 49px; top: 301px; width: 298px; }
  .rule--address { left: 353px; top: 241px; width: 262px; }
  .phone {
    left: 42px; top: 242px;
    font-family: "Crimson Text", serif; font-weight: 700; font-size: 19px;
    letter-spacing: 0.16em; color: var(--ink-soft);
  }
  .email {
    left: 19px; top: 324px;
    font-family: "Crimson Text", serif; font-weight: 600; font-size: 10.5px;
    letter-spacing: 0.06em; color: var(--ink-soft);
  }
  .pin { }
  .pin--small { left: 382px; top: 174px; width: 36px; height: 36px; }
  .pin--large { left: 368px; top: 256px; width: 64px; height: 64px; }
  .address {
    font-family: "Alegreya", serif; font-weight: 700; font-size: 14.5px;
    letter-spacing: 0.04em; line-height: 23px; color: var(--ink-soft);
  }
  .address--north { left: 443px; top: 164px; }
  .address--south { left: 452px; top: 274px; }
</style>
</head>
<body>
<main class="canvas">

  <section class="card card--front" aria-label="Business card front">
    <div class="brand brand-name">FERNWAY</div>
    <div class="brand brand-sub">CHIROPRACTIC</div>
    <div class="front-rule"></div>
    <p class="tagline">WHO WOULD YOU BE WITHOUT PAIN?</p>
    <p class="website">www.FernwayClinics.example</p>
  </section>

  <section class="card card--back" aria-label="Business card back">
    <div class="brand brand-name">FERNWAY</div>
    <div class="brand brand-sub">CHIROPRACTIC</div>

    <div class="clinic-block">
      <div>CLINIC//</div>
      <div>FERNWAY CHIROPRACTIC</div>
      <div class="doctor">DR. BRAM HOLTVICK, D.C.</div>
    </div>

    <div class="divider-v"></div>
    <div class="rule rule--phone-top"></div>
    <div class="rule rule--phone-bottom"></div>
    <div class="rule rule--address"></div>

    <p class="phone">PHONE- 971.555.0143</p>
    <p class="email">EMAIL-b.holtvick@ReliefBeginsHere.example</p>

    <svg class="pin pin--small" viewBox="0 0 40 40" aria-hidden="true">
      <ellipse cx="20" cy="32" rx="17" ry="6" fill="none" stroke="var(--accent)" stroke-width="2.5"/>
      <ellipse cx="20" cy="32" rx="9" ry="3" fill="var(--accent)"/>
      <path d="M20 31 C14 22 11 18 11 13 a9 9 0 0 1 18 0 c0 5 -3 9 -9 18z" fill="var(--accent)"/>
      <circle cx="20" cy="13" r="3.5" fill="var(--card-grey)"/>
    </svg>
    <p class="address address--north">20418 NW MARWICK ROAD<br>SUITE B<br>NORTH PLAINS, OR 97133</p>

    <svg class="pin pin--large" viewBox="0 0 40 40" aria-hidden="true">
      <ellipse cx="20" cy="32" rx="17" ry="6" fill="none" stroke="var(--accent)" stroke-width="2.5"/>
      <ellipse cx="20" cy="32" rx="9" ry="3" fill="var(--accent)"/>
      <path d="M20 31 C14 22 11 18 11 13 a9 9 0 0 1 18 0 c0 5 -3 9 -9 18z" fill="var(--accent)"/>
      <circle cx="20" cy="13" r="3.5" fill="var(--card-grey)"/>
    </svg>
    <p class="address address--south">13529 SE CALLOWAY STREET<br>PORTLAND OR 97236</p>
  </section>

</main>
</body>
</html>
```